Clear Plastic Business Card for Executives

We need a business card design for a national technology sales company that focuses on large and enterprise business. We handle every manufacturer and have clients as reputable as the KVT and Zuvora. We have a general idea of what we are looking for in the design, which is included. We are looking for a clear card, not frosted, with a microchip or motherboard design such as seen in the rough picture. The back will have select quotes we use. Our company logo is attached on the top left of the card which will be included on the card. The final design should communicate VIP level service and executive performance.
Target Market(s)
Technology executives, CIO's, CEO's
Industry/Entity Type
Business
Contact Information for Business Card
clear card for the executive level, name, office and mobile number, title, logo
Requirements
Must have
- Included RMZ logo, 2 sides, microchip/computer chip technology design, clear

```html
<!DOCTYPE html>
<html lang="en">
<head>
<meta charset="utf-8">
<title>RMZ Technologies – Business Card</title>
<link href="https://fonts.googleapis.com/css2?family=Raleway:wght@300;400;500;600&display=swap" rel="stylesheet">
<style>
  :root {
    --page: #e9e7e4;
    --clear-top: #f4f4f3;
    --clear-bottom: #d9d9d8;
    --band: #1c1c1c;
    --accent: #c8262e;
    --accent-deep: #8e1d22;
    --ink: #3a3a3a;
    --light: #f2f2f2;
    --muted: #b9b9b9;
  }
  * { box-sizing: border-box; margin: 0; padding: 0; }
  html, body { width: 804px; height: 1200px; overflow: hidden; }
  body {
    background: var(--page);
    font-family: "Raleway", Arial, sans-serif;
    position: relative;
  }
  .card {
    position: absolute;
    left: 52px;
    width: 700px;
    height: 400px;
    background: linear-gradient(180deg, var(--clear-top), var(--clear-bottom));
    box-shadow: 0 18px 40px rgba(0,0,0,.18);
    overflow: hidden;
  }
  .card--front { top: 110px; }
  .card--back { top: 660px; }

  .band {
    position: absolute;
    left: 0; right: 0; bottom: 0;
    background: var(--band);
  }
  .accent-strip {
    position: absolute;
    height: 10px;
    background: var(--accent);
  }

  /* front */
  .card--front .band { top: 258px; }
  .card--front .accent-strip { left: 40px; top: 248px; width: 430px; }

  .chip-art {
    position: absolute;
    left: 420px; top: 0;
    width: 280px; height: 248px;
    background: linear-gradient(200deg, rgba(142,29,34,.85) 0%, rgba(200,38,46,.45) 45%, rgba(200,38,46,.08) 100%);
  }
  .chip-traces {
    position: absolute;
    left: 555px; top: 258px;
    width: 125px; height: 128px;
    background: linear-gradient(180deg, rgba(200,38,46,.45), rgba(200,38,46,.1));
  }

  .brand {
    position: absolute;
    left: 60px; top: 150px;
    font-size: 30px;
    font-weight: 500;
    color: var(--ink);
    letter-spacing: .5px;
  }

  .person {
    position: absolute;
    left: 40px; top: 284px;
    display: flex; gap: 14px; align-items: flex-start;
  }
  .icon-ring {
    width: 30px; height: 30px;
    border: 1.5px solid var(--muted);
    border-radius: 50%;
    display: flex; align-items: center; justify-content: center;
    flex: none;
  }
  .icon-ring svg { width: 14px; height: 14px; fill: var(--accent); }
  .person__name {
    font-size: 19px;
    color: var(--accent);
    letter-spacing: .3px;
  }
  .person__name b { font-weight: 600; }
  .person__name span { font-weight: 400; }
  .person__title {
    font-size: 12.5px;
    color: var(--muted);
    margin: 2px 0 0 34px;
  }

  .contacts {
    position: absolute;
    left: 315px; top: 282px;
    list-style: none;
    display: flex; flex-direction: column; gap: 10px;
  }
  .contacts li {
    display: flex; align-items: center; gap: 10px;
    font-size: 13.5px; color: var(--light);
  }
  .contacts .icon-ring { width: 26px; height: 26px; }
  .contacts .icon-ring svg { width: 12px; height: 12px; }

  /* back */
  .card--back .accent-strip { left: 50px; top: 222px; width: 520px; }
  .card--back .band { top: 232px; }
  .quote {
    position: absolute;
    left: 70px; top: 278px;
    width: 560px;
    color: var(--light);
    font-size: 16px;
    line-height: 1.45;
    font-weight: 400;
  }
  .quote cite {
    display: block;
    text-align: right;
    color: var(--accent);
    font-style: normal;
    font-weight: 500;
    font-size: 14px;
    margin-top: 6px;
  }
</style>
</head>
<body>

<section class="card card--front" aria-label="Card front">
  <div class="chip-art" role="img" aria-label="Red microchip with circuit board traces"></div>
  <div class="brand">RMZ Technologies, Inc.</div>
  <div class="band"></div>
  <div class="accent-strip"></div>
  <div class="chip-traces" role="img" aria-label="Red circuit traces running down from the microchip"></div>

  <div class="person">
    <div class="icon-ring">
      <svg viewBox="0 0 16 16"><circle cx="8" cy="5" r="3.2"/><path d="M2 15c0-3.5 2.7-5.5 6-5.5s6 2 6 5.5z"/></svg>
    </div>
    <div>
      <div class="person__name"><b>DANIEL</b> <span>MERCER</span></div>
      <div class="person__title">Sales Director</div>
    </div>
  </div>

  <ul class="contacts">
    <li>
      <span class="icon-ring"><svg viewBox="0 0 16 16"><path d="M3.5 1.5l2.6 2.8-1.5 1.8c.9 2 2.5 3.6 4.5 4.5l1.8-1.5 2.8 2.6-1.7 2.6C7 13.5 2.5 9 1 3.2z"/></svg></span>
      555-208-4416
    </li>
    <li>
      <span class="icon-ring"><svg viewBox="0 0 16 16"><path d="M4.5 1h7v14h-7zM6 2.5v9.5h4V2.5z"/><circle cx="8" cy="13.4" r=".8"/></svg></span>
      555-208-4416
    </li>
    <li>
      <span class="icon-ring"><svg viewBox="0 0 16 16"><path d="M1 3.5h14v9H1zM2.2 4.5L8 9l5.8-4.5z"/></svg></span>
      daniel@rmzmail.com
    </li>
  </ul>
</section>

<section class="card card--back" aria-label="Card back">
  <div class="band"></div>
  <div class="accent-strip"></div>
  <blockquote class="quote">
    “Lorem Ipsum is simply dummy text of the printing and typesetting industry. Lorem Ipsum has been the industry's”
    <cite>Henry Caldwell</cite>
  </blockquote>
</section>

</body>
</html>
```